PEACFUL ACUPUNCTURE PRACTITIONER NEEDS A NEW COAT

I need a new design for an exiting website http://willowgateneedlework.com/ for a acupuncturist. This will be a minimalism design with lots and lots of white space. Home page and one interior page. Please keep the feeling of calm and peaceful serenity. For Color scheme: https://www.morningfernclinic.com/fertility. The bottom part of the home page with sections and links to the service pages: https://harborlotuswellness.com/. The client likes this the best: http://mfclinic.com/. I'm attaching the logo and content pages.

Target Market(s)

Women

Industry/Entity Type

Wellness, health, wellbeing, meditation

Number of Pages Required

2 page

Font styles to use
Sans Serif
Decorative

Colors

Designer to choose colors to be used in the design.

Requirements
Must have
Nice to have
• Follow new website drafts and links
Should not have
• Busy with bright colors. No poping

```html
<!DOCTYPE html>
<html lang="en">
<head>
<meta charset="utf-8">
<title>About – Willow Gate Acupuncture</title>
<link href="https://fonts.googleapis.com/css2?family=Gelasio:ital,wght@0,400;0,700;1,700&family=Pinyon+Script&display=swap" rel="stylesheet">
<style>
  :root {
    --bg: #ffffff;
    --ink: #4a4646;
    --body: #a9a38c;
    --initial: #f1e7ea;
    --mark: #b58c98;
    --rule: #9a9888;
    --photo-a: #f5e3c2;
    --photo-b: #e9c7a0;
    --photo-c: #d98a55;
  }
  * { margin: 0; padding: 0; box-sizing: border-box; }
  html, body { width: 1200px; height: 800px; overflow: hidden; background: var(--bg); }
  body { position: relative; font-family: "Gelasio", Georgia, serif; color: var(--ink); }

  .site-header { position: absolute; top: 0; left: 0; width: 1200px; height: 90px; }
  .brand { position: absolute; left: 46px; top: 24px; display: flex; align-items: center; gap: 10px; color: var(--ink); text-decoration: none; }
  .brand-dot { width: 38px; height: 38px; border-radius: 50%; background: var(--mark); opacity: .55; }
  .brand-name { font-size: 25px; font-weight: 400; line-height: 1; }
  .brand-name small { display: block; font-size: 13px; letter-spacing: 3px; margin-top: 4px; text-transform: uppercase; }

  .main-nav { position: absolute; top: 35px; left: 824px; display: flex; gap: 28px; font-size: 17px; }
  .main-nav a { color: var(--ink); text-decoration: none; }
  .main-nav .current { border-bottom: 1px solid var(--rule); padding-bottom: 1px; }
  .main-nav .has-menu { display: flex; align-items: center; gap: 7px; }
  .menu-toggle { position: absolute; left: 1119px; top: 36px; }

  .initial { position: absolute; font-family: "Pinyon Script", cursive; color: var(--initial); font-size: 118px; line-height: 1; pointer-events: none; }
  .section-title { position: absolute; font-size: 20px; font-weight: 700; font-style: italic; color: var(--ink); }
  .copy { position: absolute; font-size: 14.5px; line-height: 20.5px; color: var(--body); }

  .bio-initial { left: 22px; top: 215px; }
  .bio-title { left: 60px; top: 272px; }
  .bio-copy { left: 60px; top: 299px; width: 1060px; }

  .portrait { position: absolute; left: 56px; top: 448px; width: 410px; height: 335px; border-radius: 8px;
    background: radial-gradient(ellipse at 48% 45%, var(--photo-c) 0%, var(--photo-b) 30%, var(--photo-a) 70%); }

  .focus-initial { left: 506px; top: 405px; }
  .focus-title { left: 544px; top: 463px; }
  .focus-col-1 { left: 544px; top: 489px; width: 285px; }
  .focus-col-2 { left: 855px; top: 489px; width: 285px; }
</style>
</head>
<body>
  <header class="site-header">
    <a class="brand" href="#">
      <span class="brand-dot"></span>
      <span class="brand-name">Willow Gate<small>Acupuncture</small></span>
    </a>
    <nav class="main-nav">
      <a href="#">Home</a>
      <a href="#" class="current">About</a>
      <a href="#" class="has-menu">Treatments
        <svg width="12" height="8" viewBox="0 0 12 8"><path d="M1 1.5 6 6.5 11 1.5" fill="none" stroke="#4a4646" stroke-width="1.5"/></svg>
      </a>
    </nav>
    <svg class="menu-toggle" width="33" height="20" viewBox="0 0 33 20" aria-label="Menu">
      <path d="M0 1h33M0 9h33M0 17h33" stroke="#4a4646" stroke-width="1.5"/>
    </svg>
  </header>

  <main>
    <section class="bio">
      <span class="initial bio-initial">M</span>
      <h1 class="section-title bio-title">Mara</h1>
      <p class="copy bio-copy">Maren Holloway is a Massachusetts and California Licensed Acupuncturist and Herbalist as well as Nationally Certified in both Acupuncture and Herbal Medicine. She obtained her Masters Degree from Tall Cedar University in Santa Cruz CA and has studied at the integrated hospital in Hang Zhou China.<br>
      She has also done extensive study in Chi Nei Tsang in both the USA and Thailand.<br>
      She worked for Juniper Herb Company a leader of high quality, lab tested Chinese patented herbal formulas as a consultant to both Acupuncturists and Western MD’s.<br>
      Every year Mara commits to attending in person and virtual educational events in order to grow as a practitioner and human being.</p>
    </section>

    <section class="focus">
      <div class="portrait" role="img" aria-label="Portrait photo of the practitioner in front of a light curtain"></div>
      <span class="initial focus-initial">A</span>
      <h2 class="section-title focus-title">Area of Focus</h2>
      <p class="copy focus-col-1">“I have focused on hormonal health and fertility through bodywork, acupuncture and herbal medicine for decades.<br>
      A fascination with how the hormonal feedback loops of our bodies can be accessed through the patterns of Acupuncture led me towards an obsession with fertility and conception.<br>
      I began my training with Dr. Lena Hart in San Francisco in 1998. After completing my Masters Degree at TCU and then further study in China, I returned to CA to work with the team at Stillwater Acupuncture and Coastal Reproductive Endocrinologists. In</p>
      <p class="copy focus-col-2">&nbsp;2011 I returned to the East Coast to be closer to my family and began my private practice.<br>
      Every year I commit to continue my learning through both online classes and conferences.<br>
      I love my work so you will often find me in the office! But I can also be found hiking, camping, reading, eating vegetables, sitting quietly, feeding the birds while avoiding bears, traveling, laughing at good jokes and enjoying time with my animal, human and extended friend family.</p>
    </section>
  </main>
</body>
</html>
```